RTamberly Business Cards & Letterhead

I have a logo but need a design for some new business cards. We are a Design-Build Firm that specializes in the design and construction of commercial projects.
the cards need to be professional. no cartoon stuff.
i would like to have the cards in AI format so I can update the card as needed. Logo is provided.
Our Address is: 4183 Marwood Ln. Orin, East Varnolia 27614

```html
<!DOCTYPE html>
<html lang="en">
<head>
<meta charset="utf-8">
<title>RTamberly Business Card</title>
<link href="https://fonts.googleapis.com/css2?family=Exo+2:wght@500;600;700;800&display=swap" rel="stylesheet">
<style>
  :root {
    --page: #f4f4f4;
    --card: #ffffff;
    --ink: #2a282a;
    --panel: #231f20;
    --blue: #1a6aab;
    --blue-deep: #12406b;
    --facet: #e4e3e5;
  }
  html, body { margin: 0; padding: 0; overflow: hidden; }
  body { width: 1200px; height: 1200px; background: var(--page); }
  .artboard { display: block; width: 1200px; height: 1200px; font-family: "Exo 2", sans-serif; }
  .card-base { fill: var(--card); }
  .facet { fill: var(--facet); }
  .panel { fill: var(--panel); }
  .panel-gap { fill: var(--panel); stroke: var(--card); stroke-width: 8; }
  .accent { fill: url(#blueSweep); }
  .brand-mark { fill: var(--blue); }
  .wordmark { fill: var(--ink); font-weight: 800; font-size: 70px; letter-spacing: 1px; }
  .name-first { fill: var(--blue); }
  .name { fill: var(--ink); font-weight: 700; font-size: 42px; letter-spacing: 2px; }
  .role { fill: var(--ink); font-weight: 600; font-size: 21px; letter-spacing: 1px; }
  .role-rule { fill: url(#blueSweep); }
  .contact { fill: var(--ink); font-weight: 600; font-size: 19px; letter-spacing: 0.8px; }
  .icon-ring { fill: none; stroke: var(--blue); stroke-width: 2; }
  .icon-fill { fill: var(--blue); }
  .icon-line { fill: none; stroke: var(--blue); stroke-width: 1.6; }
</style>
</head>
<body>
<svg class="artboard" viewBox="0 0 1200 1200" xmlns="http://www.w3.org/2000/svg">
  <defs>
    <linearGradient id="blueSweep" x1="0" y1="0" x2="1" y2="1">
      <stop offset="0" stop-color="#1f78bd"/>
      <stop offset="1" stop-color="#12406b"/>
    </linearGradient>
    <clipPath id="frontClip"><rect x="203" y="102" width="794" height="453" rx="42"/></clipPath>
    <clipPath id="backClip"><rect x="203" y="645" width="794" height="450" rx="42"/></clipPath>
  </defs>

  <!-- Front of card -->
  <g class="card-front" clip-path="url(#frontClip)">
    <rect class="card-base" x="203" y="102" width="794" height="453"/>
    <polygon class="facet" points="203,102 372,102 260,310 203,285"/>
    <polygon class="facet" points="940,345 997,372 997,555 827,555"/>
    <path class="accent" d="M203,288 L295,336 C370,376 394,442 391,555 L203,555 Z"/>
    <path class="panel" d="M203,312 L283,352 C348,386 372,446 368,555 L203,555 Z"/>
    <path class="accent" d="M808,102 C800,182 850,252 922,296 L997,345 L997,102 Z"/>
    <path class="panel" d="M832,102 C826,172 862,236 926,275 L997,318 L997,102 Z"/>
    <rect class="brand-mark" x="348" y="318" width="42" height="42"/>
    <text class="wordmark" x="404" y="360">RTAMBERLY</text>
  </g>

  <!-- Back of card -->
  <g class="card-back" clip-path="url(#backClip)">
    <rect class="card-base" x="203" y="645" width="794" height="450"/>
    <polygon class="facet" points="272,645 562,645 440,786"/>
    <path class="accent" d="M203,645 L262,645 L480,840 C562,915 566,1010 526,1095 L203,1095 Z"/>
    <path class="panel-gap" d="M150,645 L244,645 L456,835 C530,903 540,1000 500,1100 L150,1100 Z"/>
    <rect class="brand-mark" x="270" y="898" width="155" height="155"/>

    <text class="name" x="628" y="713"><tspan class="name-first">LOREM</tspan> IPSOME</text>
    <text class="role" x="630" y="746">GENERAL MANAGER</text>
    <rect class="role-rule" x="630" y="755" width="221" height="3"/>

    <g class="contact-phone">
      <circle class="icon-ring" cx="644" cy="848" r="13"/>
      <path class="icon-fill" d="M638,841 l4,-1 l2,4 l-2,2 c1,3 3,5 6,6 l2,-2 l4,2 l-1,4 c-8,0 -15,-7 -15,-15 z"/>
      <text class="contact" x="675" y="855">0145 672 318</text>
    </g>
    <g class="contact-mail">
      <circle class="icon-ring" cx="644" cy="895" r="13"/>
      <rect class="icon-fill" x="636" y="889" width="16" height="11" rx="1"/>
      <path d="M636,890 l8,6 l8,-6" fill="none" stroke="#fff" stroke-width="1.3"/>
      <text class="contact" x="675" y="902">loremipsom@rtamberly.com</text>
    </g>
    <g class="contact-address">
      <circle class="icon-ring" cx="644" cy="942" r="13"/>
      <path class="icon-line" d="M644,952 c-4,-5 -7,-8 -7,-12 a7,7 0 0 1 14,0 c0,4 -3,7 -7,12 z"/>
      <circle class="icon-fill" cx="644" cy="940" r="2.5"/>
      <text class="contact" x="675" y="949">4183 Marwood Ln. Orin,</text>
      <text class="contact" x="675" y="976">East Varnolia 27614</text>
    </g>
    <g class="contact-web">
      <circle class="icon-ring" cx="644" cy="1012" r="12"/>
      <ellipse class="icon-line" cx="644" cy="1012" rx="5" ry="12"/>
      <path class="icon-line" d="M632,1012 h24 M634,1005 h20 M634,1019 h20"/>
      <text class="contact" x="680" y="1019">www.rtamberly.com</text>
    </g>
  </g>
</svg>
</body>
</html>
```